Tarnwick is a steel frame construction company that builds residential and commercial homes

1. Homepage (we are after a basic website)
Hero Section:
A full-width image or video showcasing steel frames in construction or a finished project.
Tagline: Short, impactful tagline (e.g., "Strong Structures for Tomorrow").
Call-to-Action (CTA): A prominent "Get a Quote" or "Contact Us" button.
About Us (Snapshot Section):

A few lines about the company, emphasizing experience, certifications, and commitment to quality.
Include a "Learn More" button linking to the detailed About Us page.
Products/Services Section:

Feature the main products like steel frames for industrial, residential, and commercial projects.
Each category should have a "Learn More" link to a dedicated product page.
Project Showcase/Portfolio:

Display 2-3 featured projects with images, descriptions, and a "View All Projects" button.
Certifications & Partners:

Display logos of certifications (QSB, local building standards) and partnerships with construction companies or industry bodies.
Footer:

Contact information, quick links (Home, About, Products, Services, Contact), and social media icons.
2. Products Page
Overview:

A grid or list layout showing different steel frame products or services.
Each product should have a title, brief description, and a thumbnail image.
Individual Product Pages:

Detailed information on specific products (e.g., “Steel Frames for Residential Construction”):
Features: Highlight specific features like durability, eco-friendliness, precision, etc.
Technical Specs: Material grades, dimensions, finishes available.
Case Studies: A couple of client testimonials or case studies of where this product was used.
Downloadable Resources:

Technical datasheets or catalogs for users to download.
Include a form to capture user information before they download the document (optional for lead generation).
3. Projects/Portfolio Page
Gallery of Projects:
Display completed projects with high-quality images, each linked to a project detail page.
Filter options (e.g., industrial, residential, commercial).
Project Detail Pages:
A detailed description of the project, challenges, and how the steel frames were used.
other website we liked are:
https://www.tarnwickbuilds.example/
https://orlenbayhomes.example/

1. Objective:
Create an informative, professional, and visually appealing website that promotes steel frame construction solutions, showcasing the company’s offerings, expertise, and projects.
The website should highlight the benefits of steel frames (e.g., durability, sustainability, and cost-efficiency) and cater to both B2B and B2C clients.
2. Target Audience:
Primary: Architects, builders, and construction companies.
Secondary: Homeowners, investors, and property developers looking for modern, durable construction solutions.

```html
<!DOCTYPE html>
<html lang="en">
<head>
<meta charset="utf-8">
<title>Tarnwick — Steel Frame Construction</title>
<link href="https://fonts.googleapis.com/css2?family=Figtree:wght@400;500;600;700;800&family=Poppins:wght@700&display=swap" rel="stylesheet">
<style>
:root{
  --blue:#1570bd;
  --blue-deep:#0f5ea3;
  --ink:#111418;
  --text:#2c2f33;
  --muted:#5a5f66;
  --grey-bg:#efefef;
  --footer:#0b0e13;
  --white:#ffffff;
  --line:#d9dde2;
}
*{margin:0;padding:0;box-sizing:border-box}
html,body{width:1200px;height:3280px;overflow:hidden}
body{position:relative;font-family:"Figtree",sans-serif;color:var(--text);background:var(--white)}
.abs{position:absolute}
a{color:inherit;text-decoration:none}

/* header */
.site-header{position:absolute;left:0;top:0;width:1200px;height:62px;background:var(--white)}
.brand{position:absolute;display:flex;align-items:center;gap:8px;font-weight:800;letter-spacing:.5px}
.brand-mark{width:14px;height:14px;background:var(--blue)}
.site-header .brand{left:106px;top:17px;font-size:24px;color:var(--blue)}
.nav-link{position:absolute;top:24px;font-size:10.5px;font-weight:600;color:var(--ink)}
.nav-link.active{color:var(--blue)}
.nav-phone{color:var(--blue);display:flex;align-items:center;gap:4px}
.btn{position:absolute;display:flex;align-items:center;justify-content:center;background:var(--blue);color:var(--white);font-weight:700;font-size:10px;border-radius:2px}

/* hero */
.hero{position:absolute;left:0;top:62px;width:1200px;height:438px;
  background:linear-gradient(180deg,#3e6fae 0%,#6e97c5 35%,#8fa7b4 58%,#5d7a3e 78%,#8a7652 100%)}
.hero-shade{position:absolute;inset:0;background:rgba(10,25,50,.25)}
.hero-eyebrow{position:absolute;top:134px;width:1200px;text-align:center;color:var(--white);font-weight:700;font-size:14px;letter-spacing:4px}
.hero-title{position:absolute;top:160px;width:1200px;text-align:center;color:var(--white);font-family:"Poppins",sans-serif;font-weight:700;font-size:40px;line-height:50px}

/* about */
.about{position:absolute;left:0;top:500px;width:1200px;height:543px;background:var(--grey-bg)}
.eyebrow{font-size:11px;font-weight:600;color:var(--blue)}
.about-title{font-size:26px;font-weight:500;color:var(--ink);line-height:31px;width:400px}
.about-copy{font-size:9.5px;line-height:15px;color:var(--ink);width:380px}

/* products */
.section-title{position:absolute;width:1200px;text-align:center;font-size:25px;font-weight:500;color:var(--ink);line-height:29px}
.section-eyebrow{position:absolute;width:1200px;text-align:center;font-size:11px;font-weight:600;color:var(--blue)}
.product-card{position:absolute;top:1251px;width:250px;height:336px;border:1px solid var(--blue);border-bottom:none;background:var(--white);overflow:hidden}
.product-card .kicker{position:absolute;left:18px;top:16px;font-size:9.5px;color:var(--blue);font-weight:500}
.product-card h3{position:absolute;left:18px;top:35px;font-size:20px;font-weight:800;color:var(--ink);letter-spacing:.3px}
.product-card p{position:absolute;left:18px;top:72px;width:212px;font-size:9.5px;line-height:15px;color:var(--muted)}
.product-card .read{position:absolute;left:18px;top:146px;font-size:10px;font-weight:700;color:var(--blue)}
.product-card svg.photo{position:absolute;left:0;bottom:0}

/* projects */
.projects{position:absolute;left:0;top:1661px;width:1200px;height:644px;background:var(--blue)}
.project{position:absolute;top:157px;width:312px;height:312px}
.project-caption{position:absolute;top:438px;width:250px;height:73px;background:var(--blue);color:var(--white);text-align:center;font-size:14px;line-height:20px;padding-top:16px;border-bottom:1px solid var(--white)}
.drag{position:absolute;left:913px;top:132px;width:48px;height:48px;border-radius:50%;background:var(--white);color:var(--blue);font-size:9px;font-weight:600;display:flex;align-items:center;justify-content:center}

/* partners */
.tab{position:absolute;top:2463px;width:100px;text-align:center;font-size:10.5px;padding-bottom:8px}
.partner{position:absolute;top:2520px;width:144px;height:83px;background:var(--white);border-radius:6px;box-shadow:0 4px 14px rgba(0,0,0,.07);display:flex;align-items:center;justify-content:center}
.partner-badge{width:84px;height:26px;border-radius:4px;background:#dde3ea}

/* footer */
.site-footer{position:absolute;left:0;top:2943px;width:1200px;height:337px;background:var(--footer);color:var(--white)}
.site-footer h4{position:absolute;top:70px;font-size:14px;font-weight:600}
.foot-item{position:absolute;font-size:11px;color:#e6e8eb;display:flex;align-items:center;gap:6px}
.social{position:absolute;top:171px;width:30px;height:30px;border-radius:50%;background:#3a3e45}
</style>
</head>
<body>

<header class="site-header">
  <div class="brand"><span class="brand-mark"></span>Tarnwick</div>
  <a class="nav-link active" style="left:560px">Home</a>
  <a class="nav-link" style="left:613px">About</a>
  <a class="nav-link" style="left:666px">Products</a>
  <a class="nav-link" style="left:734px">Services</a>
  <a class="nav-link" style="left:799px">Contact Us</a>
  <a class="nav-link nav-phone" style="left:883px">
    <svg width="9" height="9" viewBox="0 0 24 24"><path d="M6.6 10.8a15 15 0 0 0 6.6 6.6l2.2-2.2c.3-.3.7-.4 1-.2 1.1.4 2.3.6 3.6.6.6 0 1 .4 1 1V20c0 .6-.4 1-1 1A17 17 0 0 1 3 4c0-.6.4-1 1-1h3.5c.6 0 1 .4 1 1 0 1.3.2 2.5.6 3.6.1.3 0 .7-.2 1z" fill="none" stroke="currentColor" stroke-width="2"/></svg>555-210-4718</a>
  <a class="btn" style="left:994px;top:15px;width:88px;height:31px">Get a Quote</a>
</header>

<section class="hero" role="img" aria-label="Light-gauge steel house frames under construction against a blue sky with trees">
  <div class="hero-shade"></div>
  <div class="hero-eyebrow">TARNWICK</div>
  <h1 class="hero-title">Strong structures for<br>tomorrow</h1>
  <a class="btn" style="left:557px;top:279px;width:86px;height:31px">Get a Quote</a>
</section>

<section class="about">
  <svg class="abs" style="left:200px;top:76px" width="350" height="395" viewBox="0 0 350 395">
    <path d="M68 0H300L348 46V329" fill="none" stroke="var(--blue)" stroke-width="1.4"/>
  </svg>
  <svg class="abs" style="left:200px;top:95px" width="330" height="373" viewBox="0 0 330 373" role="img" aria-label="Steel building frame against a sky with sunlight breaking through">
    <defs><linearGradient id="aboutPhoto" x1="0" y1="0" x2="0" y2="1">
      <stop offset="0" stop-color="#9fc0e0"/><stop offset=".55" stop-color="#5f86b3"/><stop offset=".75" stop-color="#c99a6a"/><stop offset="1" stop-color="#40618a"/></linearGradient></defs>
    <path d="M0 0H300L330 32V373H0Z" fill="url(#aboutPhoto)"/>
  </svg>
  <div class="abs eyebrow" style="left:611px;top:143px">About us</div>
  <h2 class="abs about-title" style="left:611px;top:173px">Lorem Ipsum is simply work dummy text of the printing and typesetting industry.</h2>
  <p class="abs about-copy" style="left:611px;top:284px">There are many variations of passages of lorem ipsum available, but the majority have suffered alteration in some form, by injected humour, or randomised words which don't look even slightly believable. If you are going to use a passage of lorem ipsum, you need to be sure there isn't anything embarrassing hidden</p>
  <a class="btn" style="left:611px;top:370px;width:100px;height:29px">Learn more ↗</a>
</section>

<div class="section-eyebrow" style="top:1119px">Products/Services</div>
<h2 class="section-title" style="top:1140px">The most advanced cold-formed<br>steel building system</h2>

<article class="product-card" style="left:200px">
  <div class="kicker">Steel Frames for</div>
  <h3>INDUSTRIAL</h3>
  <p>Lorem ipsum is simply dummy text of the printing and typesetting industry. lorem ipsum has been the industry's standard dummy text ever since unknown...</p>
  <a class="read">Read More ↗</a>
  <svg class="photo" width="250" height="186" viewBox="0 0 250 186" role="img" aria-label="Industrial steel frame with scaffolding">
    <defs><linearGradient id="pInd" x1="0" y1="0" x2="1" y2="1"><stop offset="0" stop-color="#c8d6ee"/><stop offset="1" stop-color="#3e58a8"/></linearGradient></defs>
    <path d="M0 40L250 0V186H0Z" fill="url(#pInd)"/></svg>
</article>
<article class="product-card" style="left:475px">
  <div class="kicker">Steel Frames for</div>
  <h3>RESIDENTIAL</h3>
  <p>Lorem ipsum is simply dummy text of the printing and typesetting industry. lorem ipsum has been the industry's standard dummy text ever since unknown...</p>
  <a class="read">Read More ↗</a>
  <svg class="photo" width="250" height="186" viewBox="0 0 250 186" role="img" aria-label="Brick house with a steel roof frame">
    <defs><linearGradient id="pRes" x1="0" y1="0" x2="0" y2="1"><stop offset="0" stop-color="#3f78c4"/><stop offset=".5" stop-color="#8aa3bd"/><stop offset="1" stop-color="#b45a3c"/></linearGradient></defs>
    <path d="M0 40L250 0V186H0Z" fill="url(#pRes)"/></svg>
</article>
<article class="product-card" style="left:750px">
  <div class="kicker">Steel Frames for</div>
  <h3>COMMERCIAL</h3>
  <p>Lorem ipsum is simply dummy text of the printing and typesetting industry. lorem ipsum has been the industry's standard dummy text ever since unknown...</p>
  <a class="read">Read More ↗</a>
  <svg class="photo" width="250" height="186" viewBox="0 0 250 186" role="img" aria-label="Long commercial steel frame building">
    <defs><linearGradient id="pCom" x1="0" y1="0" x2="0" y2="1"><stop offset="0" stop-color="#dfe7c8"/><stop offset=".5" stop-color="#8c9aae"/><stop offset="1" stop-color="#3b3f47"/></linearGradient></defs>
    <path d="M0 40L250 0V186H0Z" fill="url(#pCom)"/></svg>
</article>

<section class="projects">
  <div class="section-eyebrow" style="top:82px;color:var(--white)">Our Project</div>
  <h2 class="section-title" style="top:106px;color:var(--white)">Explore our latest work</h2>

  <svg class="project" style="left:-232px" width="312" height="312" viewBox="0 0 312 312" role="img" aria-label="Grey steel-clad industrial building"><path d="M0 0H270L312 42V312H0Z" fill="#8b98a8"/></svg>
  <svg class="project" style="left:106px" width="312" height="312" viewBox="0 0 312 312" role="img" aria-label="Modern timber-clad steel frame building"><defs><linearGradient id="pj1" x1="0" y1="0" x2="0" y2="1"><stop offset="0" stop-color="#dfe6ee"/><stop offset=".6" stop-color="#8a7a66"/><stop offset="1" stop-color="#6f6a64"/></linearGradient></defs><path d="M0 0H270L312 42V312H0Z" fill="url(#pj1)"/></svg>
  <svg class="project" style="left:443px" width="312" height="312" viewBox="0 0 312 312" role="img" aria-label="Warehouse with yellow entrance portal"><defs><linearGradient id="pj2" x1="0" y1="0" x2="0" y2="1"><stop offset="0" stop-color="#b9d3ef"/><stop offset=".55" stop-color="#9aa0a8"/><stop offset="1" stop-color="#8a8c8f"/></linearGradient></defs><path d="M0 0H270L312 42V312H0Z" fill="url(#pj2)"/></svg>
  <svg class="project" style="left:781px" width="312" height="312" viewBox="0 0 312 312" role="img" aria-label="Blue and grey steel-clad industrial building"><defs><linearGradient id="pj3" x1="0" y1="0" x2="0" y2="1"><stop offset="0" stop-color="#7fa6d6"/><stop offset=".45" stop-color="#4a6ea8"/><stop offset="1" stop-color="#9aa2ad"/></linearGradient></defs><path d="M0 0H270L312 42V312H0Z" fill="url(#pj3)"/></svg>
  <svg class="project" style="left:1119px" width="312" height="312" viewBox="0 0 312 312" role="img" aria-label="Modern timber-clad steel frame building"><path d="M0 0H270L312 42V312H0Z" fill="#8a7a66"/></svg>

  <div class="project-caption" style="left:-200px">There are many variations<br>of passages</div>
  <div class="project-caption" style="left:138px">There are many variations<br>of passages</div>
  <div class="project-caption" style="left:475px">There are many variations<br>of passages</div>
  <div class="project-caption" style="left:813px">There are many variations<br>of passages</div>
  <div class="project-caption" style="left:1150px">There are many variations<br>of passages</div>

  <div class="drag">← Drag →</div>
  <a class="btn" style="left:544px;top:543px;width:112px;height:32px;background:var(--white);color:var(--blue)">View All Projects</a>
</section>

<div class="abs" style="left:0;top:2675px;width:1200px;height:268px;background:linear-gradient(180deg,#ffffff 0%,#e9eef4 60%,#dfe6ee 100%)" role="img" aria-label="Faint view of a steel roof truss from below"></div>

<div class="section-eyebrow" style="top:2381px">Tarnwick</div>
<h2 class="section-title" style="top:2403px">Certifications &amp; partners</h2>
<div class="tab" style="left:494px;color:var(--ink);border-bottom:1px solid var(--ink)">Certifications</div>
<div class="tab" style="left:606px;color:var(--blue);border-bottom:1px solid var(--blue)">Partners</div>

<div class="partner" style="left:200px"><span class="partner-badge"></span></div>
<div class="partner" style="left:364px"><span class="partner-badge"></span></div>
<div class="partner" style="left:527px"><span class="partner-badge"></span></div>
<div class="partner" style="left:692px"><span class="partner-badge"></span></div>
<div class="partner" style="left:855px"><span class="partner-badge"></span></div>

<svg class="abs" style="left:557px;top:2637px" width="86" height="26" viewBox="0 0 86 26">
  <rect x="0" y="0" width="86" height="26" rx="13" fill="#fff" stroke="#eceff2"/>
  <circle cx="15" cy="13" r="3" fill="#c6ccd3"/><circle cx="33" cy="13" r="3" fill="var(--blue)"/>
  <circle cx="52" cy="13" r="3" fill="#c6ccd3"/><circle cx="71" cy="13" r="3" fill="#c6ccd3"/>
</svg>

<footer class="site-footer">
  <div class="brand" style="left:200px;top:90px;font-size:36px;color:var(--blue)"><span class="brand-mark" style="width:22px;height:22px"></span>Tarnwick</div>
  <span class="social" style="left:254px"></span>
  <span class="social" style="left:291px;background:var(--blue)"></span>
  <span class="social" style="left:328px"></span>
  <span class="social" style="left:366px"></span>

  <h4 style="left:566px">Contact Us</h4>
  <div class="foot-item" style="left:566px;top:100px;font-size:14px">
    <svg width="11" height="11" viewBox="0 0 24 24"><path d="M6.6 10.8a15 15 0 0 0 6.6 6.6l2.2-2.2c.3-.3.7-.4 1-.2 1.1.4 2.3.6 3.6.6.6 0 1 .4 1 1V20c0 .6-.4 1-1 1A17 17 0 0 1 3 4c0-.6.4-1 1-1h3.5c.6 0 1 .4 1 1 0 1.3.2 2.5.6 3.6.1.3 0 .7-.2 1z" fill="none" stroke="var(--blue)" stroke-width="2.4"/></svg>555.210.4718</div>
  <div class="foot-item" style="left:566px;top:132px">
    <svg width="10" height="10" viewBox="0 0 24 24"><rect x="2" y="5" width="20" height="14" rx="2" fill="none" stroke="var(--blue)" stroke-width="2.4"/><path d="M2 6l10 7 10-7" fill="none" stroke="var(--blue)" stroke-width="2.4"/></svg>info@tarnwick.example</div>
  <div class="foot-item" style="left:566px;top:161px;align-items:flex-start;line-height:22px">
    <svg width="10" height="12" viewBox="0 0 24 28" style="margin-top:5px"><path d="M12 27s9-9 9-16a9 9 0 0 0-18 0c0 7 9 16 9 16z" fill="none" stroke="var(--blue)" stroke-width="2.6"/><circle cx="12" cy="11" r="3" fill="var(--blue)"/></svg>
    <span>48 Ferrow Lane, Unit 2, Halden<br>HL 20417</span></div>

  <h4 style="left:819px">Quick links</h4>
  <a class="foot-item" style="left:819px;top:102px">Home</a>
  <a class="foot-item" style="left:819px;top:125px">About</a>
  <a class="foot-item" style="left:819px;top:147px">Products</a>
  <a class="foot-item" style="left:819px;top:170px">Services</a>
  <a class="foot-item" style="left:819px;top:192px">Contact</a>
  <a class="foot-item" style="left:882px;top:102px">Terms and Conditions</a>
  <a class="foot-item" style="left:882px;top:125px">Privacy Policy</a>

  <div class="foot-item" style="left:200px;top:275px;font-size:10px;gap:0">© 2024&nbsp;<span style="color:var(--blue)">Tarnwick</span>&nbsp;- All Rights Reserved</div>
  <svg class="abs" style="left:1084px;top:270px" width="18" height="20" viewBox="0 0 18 20"><path d="M9 0L18 20L9 15L0 20Z" fill="var(--blue)"/></svg>
</footer>

</body>
</html>
```